New Business Card Design Project

Use the flyer uploaded and website www.brightoakbuilders.com for inspiration.
List Our Services on Backside of business cards
Martin Hollis
Harborline Renovations Inc.
Licensed General Contractors
858-471-9063

Contact Information for Business Card

Use the flyer uploaded and website www.brightoakbuilders.com for inspiration. List Our Services on Backside of business cards Martin Hollis Harborline Renovations Inc. Licensed General Contractors 858-471-9063

```html
<!DOCTYPE html>
<html lang="en">
<head>
<meta charset="utf-8">
<title>Harborline Renovations – Business Card</title>
<link href="https://fonts.googleapis.com/css2?family=Montserrat:wght@400;500;700;800&family=Oswald:wght@500&family=Saira+Condensed:wght@600&display=swap" rel="stylesheet">
<style>
  :root {
    --page-bg: #e9e9eb;
    --card-bg: #000000;
    --stripe-grey: #c4c4c4;
    --stripe-blue: #0a4fa8;
    --accent-cyan: #27a6e0;
    --text-white: #ffffff;
    --text-soft: #e6e6e6;
  }
  * { margin: 0; padding: 0; box-sizing: border-box; }
  html, body {
    width: 1004px;
    height: 1200px;
    overflow: hidden;
    background: var(--page-bg);
    font-family: "Montserrat", Arial, sans-serif;
  }
  .card {
    position: absolute;
    left: 125px;
    width: 752px;
    height: 432px;
    background: var(--card-bg);
    overflow: hidden;
  }
  .card--front { top: 154px; }
  .card--back { top: 630px; }

  .card__stripes {
    position: absolute;
    inset: 0;
    width: 100%;
    height: 100%;
  }

  .brand-name {
    position: absolute;
    color: var(--text-white);
    font-family: "Montserrat", Arial, sans-serif;
    font-weight: 500;
    letter-spacing: 0.06em;
    text-transform: uppercase;
    white-space: nowrap;
    transform: translateX(-50%);
  }
  .card--front .brand-name { left: 374px; top: 258px; font-size: 24px; }
  .card--back .brand-name { left: 213px; top: 140px; font-size: 17px; }

  .contact {
    position: absolute;
    left: 80px;
    top: 0;
    width: 300px;
    color: var(--text-white);
  }
  .contact__name {
    position: absolute;
    top: 210px;
    font-size: 33px;
    font-weight: 800;
    white-space: nowrap;
    letter-spacing: 0.01em;
  }
  .contact__company {
    position: absolute;
    top: 268px;
    font-family: "Saira Condensed", "Arial Narrow", sans-serif;
    font-weight: 600;
    font-size: 24px;
    line-height: 1.2;
    white-space: nowrap;
  }
  .contact__licence {
    position: absolute;
    top: 302px;
    font-size: 14px;
    color: var(--accent-cyan);
    white-space: nowrap;
  }
  .contact__phone {
    position: absolute;
    top: 322px;
    font-size: 27px;
    font-weight: 700;
    white-space: nowrap;
  }
  .contact__web {
    position: absolute;
    top: 358px;
    font-size: 11.5px;
    color: var(--accent-cyan);
    white-space: nowrap;
  }

  .services {
    position: absolute;
    left: 447px;
    top: 103px;
  }
  .services__headline {
    font-family: "Oswald", "Arial Narrow", sans-serif;
    font-weight: 500;
    font-size: 28px;
    color: var(--text-soft);
    letter-spacing: 0.01em;
    line-height: 1.2;
    transform: scaleX(0.9);
    transform-origin: left;
    white-space: nowrap;
  }
  .services__title {
    margin-top: 14px;
    font-size: 17px;
    font-weight: 700;
    color: var(--accent-cyan);
  }
  .services__list {
    list-style: none;
    margin-top: 7px;
    margin-left: 9px;
    font-size: 12.3px;
    line-height: 16.9px;
    color: var(--accent-cyan);
  }
</style>
</head>
<body>

  <section class="card card--front" aria-label="Card front">
    <svg class="card__stripes" viewBox="0 0 752 432" aria-hidden="true">
      <polygon fill="var(--stripe-grey)" points="0,150 520,0 566,0 0,168"/>
      <polygon fill="var(--stripe-blue)" points="22,432 22,180 652,0 680,0 35,190 35,432"/>
    </svg>
    <div class="brand-name">Harborline Renovations</div>
  </section>

  <section class="card card--back" aria-label="Card back">
    <svg class="card__stripes" viewBox="0 0 752 432" aria-hidden="true">
      <polyline fill="none" stroke="var(--accent-cyan)" stroke-width="4" points="401,432 401,82 558,0"/>
    </svg>

    <div class="brand-name">Harborline Renovations</div>

    <div class="contact">
      <h1 class="contact__name">MARTIN HOLLIS</h1>
      <p class="contact__company">Harborline Renovations Inc.</p>
      <p class="contact__licence">Licensed General Contractors</p>
      <p class="contact__phone">858-471-9063</p>
      <p class="contact__web">www.brightoakbuilders.com</p>
    </div>

    <div class="services">
      <h2 class="services__headline">REMODELLING EXPERTS</h2>
      <h3 class="services__title">OUR SERVICES</h3>
      <ul class="services__list">
        <li>- Remodel: Kitchen and Bath</li>
        <li>- Painting: Interior and Exterior</li>
        <li>- Flooring: Carpet, Vinyl, Wood</li>
        <li>- Window &amp; Door Replacement</li>
        <li>- Plumbing: Repairs and Upgrades</li>
        <li>- Energy-Efficient Upgrades</li>
        <li>- Deck &amp; Patio Construction</li>
        <li>- Water &amp; Mold Damage</li>
        <li>- Garage Renovation.</li>
      </ul>
    </div>
  </section>

</body>
</html>
```